Halvern Ditchworks LTD - website for irrigation & Landscape Lighting & Buried service wire

Looking for a website to help promote my business with Irrigation (installation, service, etc) and buried service wire/drainage solutions.

Commercial/Residential

Landscape lighting.

I’ll get photos in the trucks and trailers to upload as well maybe the machine as well.

Target Market(s)

Homeowners who want green grass and beautiful gardens. Beautiful landscape lighting

Industry/Entity Type

Irrigation systems and landscape lighting and buried service wire to homes and offering Drainage soltions.

Coding

Coded - Design and coding required

Number of Pages Required

4 page

Colors
F0912C
F2A743
F7CA91
FBE8D2
FDF5EE

Requirements
Must have
• was hoping to link up my email on halvernditchworks@mailbarn.net with the website if possible.
Nice to have
• Page for Irrigation, page for landscape lighting, page buried service wire & drainage soltions.

```html
<!DOCTYPE html>
<html lang="en">
<head>
<meta charset="utf-8">
<title>Halvern Ditchworks LTD — Irrigation, Landscape Lighting &amp; Buried Service Wire</title>
<link rel="stylesheet" href="https://fonts.googleapis.com/css2?family=Noto+Serif:wght@400;700&family=Roboto:wght@400;500&family=Kalam:wght@400;700&display=swap">
<style>
:root{
  --orange:#F0912C;
  --orange-deep:#EE6A2E;
  --amber:#F2A743;
  --peach:#F7CA91;
  --cream:#FBE8D2;
  --ivory:#FDF5EE;
  --ink:#1d1d1d;
  --text:#333333;
  --grey-band:#6f6f6f;
  --grey-card:#7c7c7c;
  --black:#000000;
  --white:#ffffff;
  --star:#f5b400;
}
*{margin:0;padding:0;box-sizing:border-box}
html,body{width:1200px;height:3598px;overflow:hidden;background:var(--white)}
body{position:relative;font-family:"Noto Serif",serif;color:var(--text)}
.abs{position:absolute}

/* top bar */
.topbar{left:0;top:0;width:1200px;height:64px;background:var(--orange);color:var(--white);font-size:12px}
.topbar .item{position:absolute;top:22px;display:flex;align-items:center;gap:10px}
.topbar svg{width:16px;height:16px}
.navbar{left:0;top:64px;width:1200px;height:56px;background:var(--white);box-shadow:0 1px 3px rgba(0,0,0,.08);z-index:2}
.navbar a{position:absolute;top:18px;font-size:15px;color:var(--ink);text-decoration:none}
.brand-tab{left:514px;top:0;width:172px;height:154px;z-index:3}
.brand-tab svg{position:absolute;inset:0}
.brand-name{position:absolute;left:0;top:52px;width:172px;text-align:center;font-family:"Noto Serif",serif;font-weight:700;color:var(--orange-deep);font-size:22px;line-height:1.15;letter-spacing:1px}
.brand-name small{display:block;font-size:12px;letter-spacing:2px}

/* hero */
.hero{left:0;top:120px;width:1200px;height:618px}
.hero-photo{position:absolute;inset:0;background:linear-gradient(100deg,#c99a2a 0%,#d8a835 30%,#a7a12f 55%,#c9c7b6 75%,#9e8c3c 100%)}
.hero svg{position:absolute;left:0;top:0}
.hero h1{position:absolute;left:115px;top:140px;font-size:38px;font-weight:700;color:var(--white)}
.hero .sub{position:absolute;left:116px;top:208px;font-size:21px;font-weight:700;color:var(--white);line-height:34px}
.btn{position:absolute;display:flex;align-items:center;justify-content:center;background:var(--orange-deep);color:var(--white);border-radius:5px;font-family:"Roboto",sans-serif;font-weight:500;font-size:15px;text-decoration:none}
.hero .btn{left:116px;top:288px;width:126px;height:40px;font-family:"Noto Serif",serif;font-weight:400}

/* about */
.about-img1{left:134px;top:824px;width:381px;height:323px;background:linear-gradient(135deg,#a98a5a,#6b5a44 55%,#cdb58d)}
.about-img2{left:334px;top:992px;width:248px;height:217px;background:var(--white);padding:5px}
.about-img2 div{width:100%;height:100%;background:linear-gradient(160deg,#7fae3e,#3f7a23 60%,#e06b2a)}
.about h2,.sec-title{font-weight:700;color:var(--ink);font-size:32px}
.about h2{left:645px;top:815px}
.about-copy{left:645px;top:877px;width:440px}
.about-copy p{font-size:14.6px;line-height:25.7px;color:var(--text)}
.about-copy p + p{margin-top:15px}
.about .btn{left:642px;top:1162px;width:126px;height:42px}

/* gallery */
.gallery{left:0;top:1285px;width:1200px;height:685px;background:linear-gradient(180deg,#747474,#6a6a6a)}
.gallery h2{position:absolute;left:0;top:62px;width:1200px;text-align:center;font-family:"Roboto",sans-serif;font-weight:500;font-size:30px;color:var(--white);letter-spacing:1px}
.tile{position:absolute}
.gallery .btn{left:538px;top:606px;width:126px;height:41px}

/* services */
.sec-title{position:absolute;left:0;width:1200px;text-align:center}
.sec-sub{position:absolute;left:0;width:1200px;text-align:center;font-size:15.5px;line-height:24px;color:var(--text)}
.svc{position:absolute;top:2203px;width:300px;height:366px}
.svc .photo{position:absolute;left:0;top:0;width:300px;height:196px}
.svc .card-shadow{position:absolute;left:16px;top:146px;width:268px;height:220px;filter:drop-shadow(0 2px 4px rgba(0,0,0,.22))}
.svc .card{width:100%;height:100%;background:var(--white);clip-path:polygon(0 26px,100% 0,100% 100%,0 100%)}
.svc .edge{position:absolute;left:0;top:140px}
.svc h3{position:absolute;left:42px;top:218px;font-size:17px;font-weight:700;color:var(--ink);letter-spacing:.6px}
.svc p{position:absolute;left:42px;top:254px;width:230px;font-size:12.5px;line-height:20.5px;letter-spacing:.5px;color:var(--ink)}
.svc .more{position:absolute;left:142px;top:331px;width:142px;height:35px;background:var(--orange);clip-path:polygon(16px 0,100% 0,100% 100%,0 100%);color:var(--white);font-size:12px;letter-spacing:.5px;display:flex;align-items:center;justify-content:center;padding-left:14px}
.arrow{position:absolute;top:2386px;width:20px;height:30px}

/* testimonials */
.quote{position:absolute;background:var(--white);box-shadow:0 1px 8px rgba(0,0,0,.14);border-radius:3px}
.quote.active{background:var(--grey-card);color:var(--white)}
.stars{position:absolute;left:22px;top:22px;color:var(--star);font-size:18px;letter-spacing:2px}
.quote p{position:absolute;left:24px;width:200px;font-size:13.5px;line-height:24px;color:var(--ink)}
.quote.active p{color:var(--white)}
.who{position:absolute;left:28px;display:flex;align-items:center;gap:14px}
.avatar{width:60px;height:60px;border-radius:50%;background:linear-gradient(160deg,#c9c3bb,#7b6c60)}
.who b{display:block;font-family:"Kalam",cursive;font-weight:700;font-size:15px;color:var(--ink)}
.who i{display:block;font-family:"Kalam",cursive;font-style:normal;font-size:15px;color:#555}
.active .who b,.active .who i{color:var(--white)}

/* footer */
.footer{left:0;top:3217px;width:1200px;height:381px;background:var(--black);color:var(--white)}
.footer .brand{position:absolute;left:0;top:84px;width:1200px;text-align:center;font-weight:700;font-size:32px;color:var(--orange);letter-spacing:2px;line-height:1.1}
.footer .brand small{display:block;font-size:16px;letter-spacing:4px}
.footer nav a{position:absolute;top:208px;font-size:15.5px;color:var(--white);text-decoration:none}
.footer hr{position:absolute;left:0;top:296px;width:1200px;border:0;border-top:1px solid #555}
.footer .copy{position:absolute;left:0;top:326px;width:1200px;text-align:center;font-size:17px;letter-spacing:1px}
</style>
</head>
<body>

<header>
  <div class="abs topbar">
    <div class="item" style="left:126px">
      <svg viewBox="0 0 16 16"><path d="M8 1a5 5 0 0 0-5 5c0 4 5 9 5 9s5-5 5-9a5 5 0 0 0-5-5zm0 7a2 2 0 1 1 0-4 2 2 0 0 1 0 4z" fill="#fff"/></svg>
      <span>Lorem Ipsum,Lorem ipsum,USA</span>
    </div>
    <div class="item" style="left:722px">
      <svg viewBox="0 0 16 16"><path d="M3 1l3 1 1 3-2 1.5a9 9 0 0 0 4.5 4.5L11 9l3 1 1 3-2 2C7 15 1 9 1 3z" fill="#fff"/></svg>
      <span>555-014-2290</span>
    </div>
    <div class="item" style="left:896px">
      <svg viewBox="0 0 16 16"><rect x="1" y="3" width="14" height="10" fill="#fff"/><path d="M1 3l7 6 7-6" fill="none" stroke="#F0912C" stroke-width="1.3"/></svg>
      <span>halvernditchworks@mailbarn.net</span>
    </div>
  </div>
  <nav class="abs navbar">
    <a href="#" style="left:171px">Home</a>
    <a href="#" style="left:246px">Irrigation installs</a>
    <a href="#" style="left:398px">Service</a>
    <a href="#" style="left:741px">Landscape Lighting</a>
    <a href="#" style="left:908px">Fiber Optic installation</a>
  </nav>
  <div class="abs brand-tab">
    <svg width="172" height="154" viewBox="0 0 172 154"><path d="M0 0H172V122L86 154L0 122Z" fill="#fff" style="filter:drop-shadow(0 2px 3px rgba(0,0,0,.2))"/></svg>
    <div class="brand-name">HALVERN<small>DITCHWORKS LTD</small></div>
  </div>
</header>

<section class="abs hero">
  <div class="hero-photo" role="img" aria-label="Irrigation technician adjusting a sprinkler head in a sunlit green field"></div>
  <svg width="1200" height="618" viewBox="0 0 1200 618">
    <path d="M0 453 Q300 530 600 578 Q900 530 1200 453 V618 H0 Z" fill="#fff"/>
    <path d="M182 494 Q420 580 600 618 Q780 580 992 503 Q790 568 600 596 Q410 565 182 494 Z" fill="#EE6A2E"/>
  </svg>
  <h1>Homeowners who want green grass</h1>
  <div class="sub">Beautiful gardens<br>Beautiful landscape lighting</div>
  <a class="btn" href="#">GET STARTED</a>
</section>

<section class="about">
  <div class="abs about-img1" role="img" aria-label="Crew working on buried service wire at a street trench"></div>
  <div class="abs about-img2"><div role="img" aria-label="Hands fitting a sprinkler head on a hose in the grass"></div></div>
  <h2 class="abs">ABOUT US</h2>
  <div class="abs about-copy">
    <p>Lorem ipsum dolor sit amet, consectetur adipiscing elit, sed do eiusmod tempor incididunt ut labore et dolore magna aliqua. Ut enim ad minim veniam, quis nostrud exercitation ullamco laboris nisi ut aliquip ex ea commodo consequat. Duis aute irure dolor in reprehenderit in voluptate velit esse cillum dolore eu fugiat nulla pariatur</p>
    <p>Excepteur sint occaecat cupidatat non proident, sunt in culpa qui officia deserunt mollit anim id est laborum.There are many variations of passages of Lorem Ipsum available</p>
  </div>
  <a class="btn" href="#">READ MORE</a>
</section>

<section class="abs gallery">
  <h2>GALLERY</h2>
  <div class="tile" style="left:136px;top:150px;width:213px;height:176px;background:linear-gradient(150deg,#9fc7d8,#3a78a8 50%,#c98a3a)" role="img" aria-label="Repairing a leaking irrigation pipe"></div>
  <div class="tile" style="left:136px;top:340px;width:213px;height:215px;background:linear-gradient(160deg,#6d8f3a,#4f6b2c 55%,#c23b2b)" role="img" aria-label="Orange service cable coiled beside a trench"></div>
  <div class="tile" style="left:369px;top:150px;width:216px;height:241px;background:linear-gradient(160deg,#e8e2d8,#d9d2c6 50%,#e0772a)" role="img" aria-label="Fiber optic test meter on a workbench"></div>
  <div class="tile" style="left:369px;top:401px;width:216px;height:154px;background:linear-gradient(180deg,#3d4a5c,#6b5a3c 60%,#2e3324)" role="img" aria-label="House at dusk with landscape lighting"></div>
  <div class="tile" style="left:606px;top:150px;width:217px;height:153px;background:linear-gradient(180deg,#6aa0d8,#2b3c55 55%,#e3e3e0)" role="img" aria-label="Solar panels on a modern house roof"></div>
  <div class="tile" style="left:606px;top:317px;width:217px;height:238px;background:linear-gradient(90deg,#7fc042,#3b6a2a 50%,#7fc042)" role="img" aria-label="Trench in a lawn with buried blue line"></div>
  <div class="tile" style="left:847px;top:150px;width:218px;height:237px;background:linear-gradient(160deg,#9bcf4a,#3b4a42 60%,#263038)" role="img" aria-label="Planting with drip irrigation line"></div>
  <div class="tile" style="left:847px;top:403px;width:218px;height:152px;background:linear-gradient(180deg,#3d4a5c,#6b5a3c 60%,#2e3324)" role="img" aria-label="Lit home exterior at evening"></div>
  <a class="btn" href="#">VIEW MORE</a>
</section>

<section class="services">
  <h2 class="sec-title" style="top:2050px">OUR SERVICES</h2>
  <p class="sec-sub" style="top:2102px">"Lorem ipsum dolor sit amet, consectetur adipiscing elit, sed do eiusmod tempor<br>incididunt ut labore et dolore magna aliqua.</p>

  <svg class="arrow" style="left:58px" viewBox="0 0 20 30"><path d="M16 2L4 15l12 13" fill="none" stroke="#111" stroke-width="2"/></svg>
  <svg class="arrow" style="left:1110px" viewBox="0 0 20 30"><path d="M4 2l12 13L4 28" fill="none" stroke="#111" stroke-width="2"/></svg>

  <article class="svc" style="left:112px">
    <div class="photo" role="img" aria-label="Sprinkler watering a front lawn" style="background:linear-gradient(180deg,#c7b79c,#6ea63a 50%,#4f8f24)"></div>
    <div class="card-shadow"><div class="card"></div></div>
    <svg class="edge" width="300" height="40" viewBox="0 0 300 40"><path d="M16 32 L284 4" stroke="#F0912C" stroke-width="4"/></svg>
    <h3>Irrigation Installs</h3>
    <p>Lorem Ipsum dolor sit amet consectetur adipiscing elit,sed do eiusmod</p>
    <div class="more">Learn More</div>
  </article>

  <article class="svc" style="left:450px">
    <div class="photo" role="img" aria-label="Technician splicing fiber optic cable" style="background:linear-gradient(120deg,#3b4048,#6d7680 50%,#d56a2a)"></div>
    <div class="card-shadow"><div class="card"></div></div>
    <svg class="edge" width="300" height="40" viewBox="0 0 300 40"><path d="M16 32 L284 4" stroke="#F0912C" stroke-width="4"/></svg>
    <h3>Fiber Optic Installation</h3>
    <p>Lorem Ipsum dolor sit amet consectetur adipiscingelit,sed do eiusmod</p>
    <div class="more">Learn More</div>
  </article>

  <article class="svc" style="left:787px">
    <div class="photo" role="img" aria-label="Modern residential townhouses" style="background:linear-gradient(180deg,#6fa6da,#9c6a4a 55%,#4a7a34)"></div>
    <div class="card-shadow"><div class="card"></div></div>
    <svg class="edge" width="300" height="40" viewBox="0 0 300 40"><path d="M16 32 L284 4" stroke="#F0912C" stroke-width="4"/></svg>
    <h3>Residential</h3>
    <p>Lorem Ipsum dolor sit amet consectetur adipiscing elit,sed do eiusmod</p>
    <div class="more">Learn More</div>
  </article>
</section>

<section class="testimonials">
  <h2 class="sec-title" style="top:2652px">TESTIMONIALS</h2>
  <p class="sec-sub" style="top:2713px">Lorem ipsum dolor sit amet, consectetur adipiscing elit, sed do eiusmod tempor incididunt ut labore<br>et dolore magna aliqua.</p>

  <div class="quote" style="left:36px;top:2812px;width:250px;height:321px">
    <div class="stars">★★★★★</div>
    <p style="top:60px">Lorem ipsum dolor sit amet, consectetur adipiscing elit, sed do eiusmod tempor incididunt ut labore et dolore magna aliqua. Ut enim ad minim veniam</p>
    <div class="who" style="top:232px"><div class="avatar" role="img" aria-label="Client portrait"></div><div><b>Orwen</b><i>Client</i></div></div>
  </div>

  <div class="quote" style="left:327px;top:2809px;width:239px;height:269px">
    <div class="stars">★★★★★</div>
    <p style="top:48px">Lorem ipsum dolor sit amet, consectetur adipiscing elit, sed do eiusmod tempor incididunt ut labore et dolore magna aliqua.</p>
    <div class="who" style="top:184px"><div class="avatar" role="img" aria-label="Client portrait"></div><div><b>Tomas Reede</b><i>Client</i></div></div>
  </div>

  <div class="quote active" style="left:610px;top:2809px;width:251px;height:323px">
    <div class="stars">★★★★★</div>
    <p style="top:72px">Lorem ipsum dolor sit amet, consectetur adipiscing elit, sed do eiusmod tempor incididunt ut labore et dolore magna aliqua Ut enim ad minim veniam</p>
    <div class="who" style="top:230px"><div class="avatar" role="img" aria-label="Client portrait"></div><div><b>Mina Castell</b><i>Client</i></div></div>
  </div>

  <div class="quote" style="left:914px;top:2809px;width:250px;height:323px">
    <div class="stars">★★★★★</div>
    <p style="top:74px">Lorem ipsum dolor sit amet, consectetur adipiscing elit, sed do eiusmod tempor incididunt ut labore et dolore magna aliqua</p>
    <div class="who" style="top:230px"><div class="avatar" role="img" aria-label="Client portrait"></div><div><b>Jon Pellow</b><i>Client</i></div></div>
  </div>
</section>

<footer class="abs footer">
  <div class="brand">HALVERN<small>DITCHWORKS LTD</small></div>
  <nav>
    <a href="#" style="left:258px">Home</a>
    <a href="#" style="left:345px">irrigation installs</a>
    <a href="#" style="left:508px">service</a>
    <a href="#" style="left:601px">Landscape Lighting</a>
    <a href="#" style="left:780px">Fiber Optic installation</a>
  </nav>
  <hr>
  <div class="copy">Copyrights@2024HALVERN DITCHWORKS LTD.com</div>
</footer>

</body>
</html>
```